Letterhead for denture company

We need a letterhead designed for our denture company called "Brightbite" We have attached the logo and business card with the colours on them that we like

Target Market(s)

Everyone aged 45+

Industry/Entity Type

Dental Clinic

Font styles to use
Serif
Sans Serif

Colors
3276b5
f37122

Requirements
Must have
• The colours used in our business card
• Be bold and modern
• Thick fonts
• Logo
Nice to have
• Elements that could tie in nicely with any future signage or website upgrades
Should not have
• Thin font
• Should not be too busy

```html
<!DOCTYPE html>
<html lang="en">
<head>
<meta charset="utf-8">
<title>Brightbite Letterhead</title>
<link rel="stylesheet" href="https://fonts.googleapis.com/css2?family=Bitter:wght@400;700&display=swap">
<style>
  :root {
    --brand-blue: #1475bd;
    --label-blue: #2a6aa8;
    --ink: #2b2b2b;
    --arc-grey: #7a7a7a;
    --rule-grey: #bdbdbd;
    --paper: #ffffff;
  }
  * { margin: 0; padding: 0; box-sizing: border-box; }
  html, body { width: 959px; height: 1200px; overflow: hidden; background: var(--paper); }
  .letterhead { position: relative; width: 959px; height: 1200px; background: var(--paper); }

  .brand { position: absolute; left: 38px; top: 40px; width: 330px; text-align: center; }
  .brand-square { display: block; width: 70px; height: 67px; margin: 0 auto 11px; background: var(--brand-blue); }
  .brand-name {
    font-family: "Bitter", Georgia, serif; font-weight: 700; font-size: 34px;
    color: var(--brand-blue); letter-spacing: 4px; line-height: 1; text-transform: uppercase;
  }

  .contact {
    position: absolute; left: 649px; top: 52px; padding-left: 11px;
    border-left: 1px solid var(--rule-grey); list-style: none;
    font-family: "Bitter", Georgia, serif; font-size: 17px; color: var(--ink);
  }
  .contact li { line-height: 25px; white-space: nowrap; }
  .contact .label { display: inline-block; width: 27px; color: var(--label-blue); }

  .footer { position: absolute; left: 0; top: 1090px; width: 959px; height: 110px; }
  .footer svg { display: block; }
  .footer-address {
    position: absolute; left: 0; right: 0; top: 59px; text-align: center;
    font-family: "Bitter", Georgia, serif; font-size: 17.5px; color: #ffffff; letter-spacing: 0.3px;
  }
</style>
</head>
<body>
<main class="letterhead">
  <header class="brand">
    <span class="brand-square"></span>
    <div class="brand-name">Brightbite</div>
  </header>

  <ul class="contact">
    <li><span class="label">P:</span>0800 55 7000</li>
    <li><span class="label">C:</span>09 721 4403</li>
    <li><span class="label">E:</span>sam@brightbite.co.nz</li>
    <li><span class="label">W:</span>www.brightbite.co.nz</li>
  </ul>

  <footer class="footer">
    <svg width="959" height="110" viewBox="0 0 959 110">
      <path d="M0 75 Q479.5 -47 959 75 Q479.5 -18 0 75 Z" fill="var(--arc-grey)"/>
      <path d="M0 75 Q479.5 -21 959 75 L959 110 L0 110 Z" fill="var(--brand-blue)"/>
    </svg>
    <p class="footer-address">148 Harbour View Road, Kelston, Auckland 0602</p>
  </footer>
</main>
</body>
</html>
```